Event Website for the Audio & Visual Industry

Convene is an exhibition aimed at meeting the business needs of audio and visual professionals – the visitors are the ones that make purchase decisions when buying anything to do with AV installation, Lighting & Entertainment Technology, DJ Technologies and even Musical Instruments.

We need to rebuild our website to reflect the professional look but with a bit of creativity/flare that is associated with the industry.

Websites whose design is along the lines we're looking for:

• http:www.marlowtech.com.au
• http:www.quenra.com
• http://www.brightpanelfair.example/ (competitor expo, like the layout. Not fantastic though, but the best I’ve seen from the industry)
• http://www.velmora.com.au and http://www.tralvick.com.au/ (Like these brand websites, they are clean and corporate but the use of imagery allows it to have some personality)

Target Market(s)

Corporate AV End Users, Lighting Designers, Concert/Entertainment companies, Sound Engineers

Industry/Entity Type

Business

Requirements
Must have
• Refer to the current splash page – www.convene-expo.example
This is the look and feel we have developed for our brochure. We want to expand on this and create a professional corporate look and feel without alienating existing sound, light and vision sectors.

The website's focus is to register visitors to attend the show. Please include a floating 'Register Free' Call to action. Please also include floating social media buttons. For what I mean by 'floating' check out the Social media buttons on this website: http://feedlorn.example/2012/02/19/glass-tower-trailer/ (scroll down to see effect).

We'll like to include a Rotating Banner at the top.

Sponsor element at the bottom off the page.

Sign up form functionality

Menu to be: About the Show, What's On, Register, How to Exhibit, Blog, Contact us.

I would like to see designs for a content page as well as the homepage.

```html
<!DOCTYPE html>
<html lang="en">
<head>
<meta charset="utf-8">
<title>Convene 2012</title>
<link rel="stylesheet" href="https://fonts.googleapis.com/css2?family=Ubuntu:wght@400;500;700&family=Arimo:wght@400;700&display=swap">
<style>
:root{
  --page:#efefef;
  --ink:#2f2f2f;
  --ink-soft:#444;
  --white:#fff;
  --red:#e31e3a;
  --red-deep:#b40f27;
  --bar-top:#4a4a4a;
  --bar-bottom:#1f1f1f;
  --footer:#3b3b3b;
  --line:#d9d9d9;
  --yellow:#f6d21a;
}
*{box-sizing:border-box;margin:0;padding:0}
html,body{width:1200px;height:1116px;overflow:hidden;background:var(--page)}
body{font-family:"Ubuntu",sans-serif;color:var(--ink)}
.stage{position:relative;width:1105px;height:1028px;transform:scale(1.08597);transform-origin:0 0}
.abs{position:absolute}
a{color:inherit;text-decoration:none}

.utility-bar{left:0;top:0;width:1105px;height:31px;background:linear-gradient(var(--bar-top),var(--bar-bottom))}
.utility-links{right:80px;top:9px;color:var(--white);font-size:12px;font-weight:500;word-spacing:1px}
.utility-links span{margin:0 8px}

.hero-band{left:0;top:31px;width:1105px;height:105px;background:repeating-linear-gradient(135deg,rgba(255,255,255,.04) 0 2px,transparent 2px 5px),linear-gradient(var(--red),var(--red-deep))}
.event-date{left:767px;top:48px;color:var(--white);font-weight:700;font-size:23px;letter-spacing:.2px}
.event-venue{left:767px;top:76px;color:var(--white);font-size:14.5px;line-height:18px}

.brand-box{left:77px;top:0;width:217px;height:121px;background:linear-gradient(#fff 60%,#e6e6e6);border-radius:0 0 10px 10px;box-shadow:0 1px 4px rgba(0,0,0,.35)}
.brand-name{left:0;top:44px;width:217px;text-align:center;font-size:34px;font-weight:500;color:var(--ink)}

.main-nav{left:0;top:136px;width:1105px;height:35px;background:linear-gradient(#555,#222)}
.nav-item{top:10px;color:var(--white);font-size:12.5px}
.nav-item.is-active{top:0;left:68px;height:34px;width:99px;background:var(--white);color:#111;padding-top:10px;text-align:center}
.newsletter{left:916px;top:10px;color:var(--white);font-weight:700;font-size:12.5px}
.newsletter-btn{left:999px;top:142px;width:23px;height:22px;background:#e9e9e9;border-radius:2px}

.slider{left:81px;top:184px;width:930px;height:201px;border-radius:8px;overflow:hidden;background:#000;box-shadow:0 1px 3px rgba(0,0,0,.3)}
.slide-brand{left:0;top:0;width:285px;height:201px;background:radial-gradient(circle at 40% 40%,#1c1c1c,#000)}
.slide-brand-name{left:0;top:62px;width:285px;text-align:center;color:var(--white);font-size:42px;font-weight:500}
.slide-partner{left:170px;top:150px;color:#ccc;font-size:6px}
.slide-cta{left:6px;top:163px;width:273px;height:33px;border-top:1px solid #555;background:linear-gradient(#1a1a1a,#000);padding:5px 0 0 16px;font-size:17px;color:var(--yellow)}
.slide-cta b{color:var(--white);font-size:20px;font-weight:700;margin-left:4px}
.slide-photo{left:285px;top:0;width:645px;height:201px;background:linear-gradient(180deg,#5b6c86 0%,#b88a56 45%,#e7a44a 62%,#3a2614 100%)}
.slider-arrow{top:270px;width:30px;height:30px;border-radius:50%;background:var(--white);box-shadow:0 1px 3px rgba(0,0,0,.3)}

.intro{left:57px;top:398px;width:980px;height:199px;background:var(--white);border-radius:10px}
.intro h1{left:26px;top:25px;font-size:21px;line-height:26px;font-weight:700;color:var(--ink);text-transform:uppercase}
.intro p{left:26px;top:91px;width:640px;font-size:13.3px;line-height:22px;color:#222}
.photo-grid{left:674px;top:10px;width:295px;height:170px;display:grid;grid-template-columns:repeat(3,1fr);gap:2px}
.photo-grid div{background:linear-gradient(150deg,#3b3f6a,#101226 70%)}
.photo-grid div:nth-child(2n){background:linear-gradient(150deg,#8a8fa8,#1b1c2e)}
.photo-grid div:nth-child(3){background:linear-gradient(150deg,#5da0d8,#0e1a33)}

.social-float{left:1043px;top:400px;width:62px;height:197px;background:#484848;border-radius:10px 0 0 10px}
.social-float i{position:absolute;left:12px;width:33px;height:33px;border-radius:3px;background:linear-gradient(#f2f2f2,#b5b5b5)}

.features{left:57px;top:609px;width:980px;height:175px;background:var(--white);border-radius:10px 10px 0 0}
.feature-card{top:7px;height:155px;border:1px solid var(--line);background:linear-gradient(#f7f7f7,#fff 40%)}
.feature-card h2{font-weight:400;font-size:16px;line-height:26px;color:#1a1a1a;padding:12px 0 0 16px}
.feature-card h2 em{font-style:normal;color:var(--red)}
.sector-list{font-family:"Arimo",sans-serif;font-size:12px;line-height:22px;color:#111;padding:0 10px 0 15px;hyphens:auto}
.perks{display:grid;grid-template-columns:148px 1fr;row-gap:12px;padding:22px 0 0 20px;font-family:"Arimo",sans-serif;font-size:12.8px;color:#111}
.perks span::before{content:"›";font-weight:700;margin-right:4px;font-size:16px}
.download-card{left:783px;top:6px;width:183px;height:156px;border-radius:3px;overflow:hidden;box-shadow:0 1px 3px rgba(0,0,0,.4)}
.download-top{height:110px;background:linear-gradient(#e8552f,#c2253a);color:var(--white);font-size:19px;line-height:27px;padding:10px 0 0 18px}
.download-btn{height:46px;background:linear-gradient(#c4102a,#7c0818);color:var(--white);font-size:17px;padding:0 0 0 13px;display:flex;align-items:center;gap:9px}
.download-btn svg{flex:none}

.site-footer{left:0;top:782px;width:1105px;height:188px;background:repeating-linear-gradient(45deg,rgba(255,255,255,.03) 0 1px,transparent 1px 3px),var(--footer)}
.footer-nav{left:90px;top:14px;list-style:none;color:var(--white);font-size:12.5px;line-height:24.2px}
.footer-notice{left:232px;top:20px;width:470px;color:var(--white);font-family:"Arimo",sans-serif;font-size:12.2px;line-height:18px}
.follow-title{left:234px;top:108px;color:#ddd;font-size:14px}
.follow-icon{top:133px;width:28px;height:28px;border-radius:3px;background:linear-gradient(#888,#555)}
.partner-badge{left:817px;top:54px;width:183px;height:78px;background:var(--white)}
.partner-badge small{position:absolute;left:13px;top:5px;font-family:"Arimo",sans-serif;font-size:11px;color:#222}
.partner-badge i{position:absolute;left:12px;top:24px;width:158px;height:40px;background:#d6d6d6}

.legal{left:57px;top:970px;width:980px;height:58px;background:var(--white)}
.legal p{position:absolute;left:16px;top:21px;font-family:"Arimo",sans-serif;font-size:11px;color:#111}
.organiser{right:20px;top:16px;font-size:18px;font-weight:700;color:#111}
</style>
</head>
<body>
<div class="stage">

  <div class="abs utility-bar"></div>
  <div class="abs utility-links"><a href="#">Your wishlist</a><span>|</span><a href="#">Your Account</a><span>|</span><a href="#">Register Your Product</a></div>

  <div class="abs hero-band"></div>
  <div class="abs event-date">21 st-23rd AUGUST 2012</div>
  <div class="abs event-venue">Harbourside Expo Hall,<br>Darling Harbour, Australia</div>

  <div class="abs brand-box">
    <div class="abs brand-name">Convene</div>
  </div>

  <nav class="abs main-nav">
    <a class="abs nav-item is-active" href="#">About the Show</a>
    <a class="abs nav-item" style="left:199px" href="#">What's On</a>
    <a class="abs nav-item" style="left:294px" href="#">Register</a>
    <a class="abs nav-item" style="left:376px" href="#">How to Exhibit</a>
    <a class="abs nav-item" style="left:492px" href="#">Blog</a>
    <a class="abs nav-item" style="left:556px" href="#">Contact Us</a>
    <span class="abs newsletter">NEWSLETTER</span>
  </nav>
  <svg class="abs newsletter-btn" viewBox="0 0 23 22"><path d="M8 8l3.5 3 3.5-3M8 12l3.5 3 3.5-3" fill="none" stroke="#555" stroke-width="1.2"/></svg>

  <section class="abs slider">
    <div class="abs slide-brand">
      <div class="abs slide-brand-name">Convene</div>
      <div class="abs slide-partner">in association with</div>
      <a class="abs slide-cta" href="#">Click here to <b>REGISTER NOW</b></a>
    </div>
    <div class="abs slide-photo" role="img" aria-label="Harbour opera house and arch bridge lit at dusk"></div>
  </section>
  <svg class="abs slider-arrow" style="left:57px" viewBox="0 0 30 30"><path d="M17 9l-6 6 6 6" fill="none" stroke="#777" stroke-width="2"/></svg>
  <svg class="abs slider-arrow" style="left:1004px" viewBox="0 0 30 30"><path d="M13 9l6 6-6 6" fill="none" stroke="#777" stroke-width="2"/></svg>

  <section class="abs intro">
    <h1 class="abs">Australia's largest audio visual, entertainment &amp;<br>information communications technology event</h1>
    <p class="abs">With over 500 brands on display, Convene in association with AVLink Global, brings together the worlds of ICT, integrating all areas including Visual, Education, Entertainment, Audio &amp; Lighting Technology, Worship, Digital Signage and Unified Communications.</p>
    <div class="abs photo-grid">
      <div role="img" aria-label="Mixing desk on the show floor"></div>
      <div role="img" aria-label="Video wall display stand"></div>
      <div role="img" aria-label="Stage lighting rig"></div>
      <div role="img" aria-label="Moving head light fixture"></div>
      <div role="img" aria-label="Visitors walking the exhibition hall"></div>
      <div role="img" aria-label="Audio console close-up"></div>
    </div>
  </section>

  <aside class="abs social-float" aria-label="Social links">
    <i style="top:17px"></i><i style="top:60px"></i><i style="top:103px"></i><i style="top:146px"></i>
  </aside>

  <section class="abs features">
    <div class="abs feature-card" style="left:17px;width:372px">
      <h2>DISCOVER THE <em>LATEST ADVANCEMENTS IN...</em></h2>
      <p class="sector-list" lang="en">• Concert Production • AV Installation • Broadcast • Staging • Lighting &amp; Entertainment Technology • Digital Media &amp; Infor&shy;mation Services • Education Technology • Post Production • Multi&shy;media • Audio Engineering • Recording • DJ Technologies • Musical Instruments</p>
    </div>
    <div class="abs feature-card" style="left:402px;width:369px">
      <h2><em>BE PART OF AUSTRALIA'S</em> ONLY EVENT FOR THE AUDIO VISUAL &amp; ENTERTAINMENT INDUSTRY</h2>
      <div class="perks"><span>NEW LOCATION</span><span>NEW SEMINARS / AVLINK</span><span>EVEN BIGGER SHOW</span><span>EVEN MORE SUPRISES</span></div>
    </div>
    <a class="abs download-card" href="#">
      <div class="download-top">DOWNLOAD<br>THE FLOOR<br>PLAN</div>
      <div class="download-btn"><svg width="14" height="14" viewBox="0 0 14 14"><circle cx="7" cy="7" r="7" fill="#fff"/><path d="M5.5 4l3 3-3 3" fill="none" stroke="#9a0b1f" stroke-width="1.8"/></svg>DOWNLOAD</div>
    </a>
  </section>

  <footer class="abs site-footer">
    <ul class="abs footer-nav">
      <li>Home</li><li>About The Show</li><li>What's On</li><li>Register</li><li>How to Exhibit</li><li>Blog</li><li>Contact Us</li>
    </ul>
    <div class="abs footer-notice">STRICTLY TRADE ONLY. Entry is restricted to members of the ICT, Audio Visual and Entertainment industries.<br><br>Persons not in these categories, including children will not be admitted at any time.</div>
    <div class="abs follow-title">Follow Us</div>
    <i class="abs follow-icon" style="left:233px"></i>
    <i class="abs follow-icon" style="left:269px"></i>
    <i class="abs follow-icon" style="left:305px"></i>
    <div class="abs partner-badge"><small>in association with</small><i></i></div>
  </footer>

  <div class="abs legal">
    <p>© 2011 Meridian Exhibitions, Australia. All rights reserved. Level 2, 118 Quay Lane, Sydney, NSW 2000, Australia.</p>
    <div class="abs organiser">meridian</div>
  </div>

</div>
</body>
</html>
```